Boutique Health and Fitness Personal Training Studio

I would like to have a brochure designed which provides a detailed description of the services offered in my business.
I have personal training studio, We look after people from early 20's to 90's, healthy to very unhealthy.
We conduct:
A consultation
An assessment
A personalised program
Personalised training sessions
I would like to base the design around the colours of my logo (attached) and use some of (or all of) the images and information I have also attached.
I would be happy with your own images included also.

Target Market(s)

20 to 90 year olds

Industry/Entity Type

Business

Font styles to use
Serif
Sans Serif

Colors
9bcb3c
add136
cadf82
eaf2ce

Requirements
Must have
• Colour and images of fitness.
• 8.5x14 legal
• Tri fold
• 2 folds with 3 faces back n front
Nice to have
• The feeling of wellbeing
Should not have
• This is not a gym.
• It should have the feel of a private relaxed environment

```html
<!DOCTYPE html>
<html lang="en">
<head>
<meta charset="utf-8">
<title>Evergreen Wellness Studio – Tri-fold Brochure</title>
<link href="https://fonts.googleapis.com/css2?family=Open+Sans:wght@400;600;700&display=swap" rel="stylesheet">
<style>
  :root{
    --green:#9bcb3c;
    --lime:#add136;
    --sage:#cadf82;
    --mist:#eaf2ce;
    --leaf:#4f8a1e;
    --ink:#3f4a2a;
    --paper:#f3f4f2;
    --stage:#d9dedd;
  }
  *{box-sizing:border-box;margin:0;padding:0}
  html,body{width:1200px;height:900px;overflow:hidden;background:var(--stage);font-family:"Open Sans",Arial,sans-serif;color:var(--ink)}
  .sheet{position:absolute;left:255px;width:690px;height:420px;overflow:hidden;box-shadow:0 4px 14px rgba(0,0,0,.18)}
  .sheet--outside{top:20px;background:#fff}
  .sheet--inside{top:460px}
  .sheet svg.bg{position:absolute;inset:0}
  .panel{position:absolute;top:0;width:230px;height:420px}
  .p1{left:0}.p2{left:230px}.p3{left:460px}

  .studio-name{font-weight:700;color:var(--leaf);line-height:1.05;display:flex;align-items:center;gap:6px}
  .studio-name .dot{width:12px;height:12px;border-radius:50%;background:var(--green);flex:none}

  /* outside */
  .back-contact{position:absolute;left:0;right:0;top:210px;text-align:right;padding-right:28px;font-size:8px;line-height:1.45;color:var(--ink)}
  .back-contact .studio-name{justify-content:flex-end;font-size:9px;margin-bottom:4px}
  .cover-brand{position:absolute;top:36px;left:20px;right:14px}
  .cover-brand .studio-name{font-size:16px}
  .tagline{margin-top:10px;background:linear-gradient(90deg,var(--mist),var(--sage));border-top:2px solid var(--green);border-bottom:2px solid var(--green);font-size:9px;font-weight:700;color:var(--leaf);padding:3px 8px;font-style:italic}

  /* inside */
  .intro{padding:26px 18px 0 20px}
  .intro h2{font-size:17px;font-weight:400;color:var(--green);line-height:1.05}
  .intro h3{font-size:14px;font-weight:600;color:var(--leaf);margin-bottom:8px;line-height:1.05}
  .intro p{font-size:7px;line-height:1.4;margin-bottom:6px}
  .intro .gap{margin-top:14px}

  .expect{padding:22px 16px 0 16px;color:#2f3a18}
  .expect h2{font-size:18px;font-weight:400;color:#fff;margin-bottom:6px}
  .expect h4{font-size:8px;font-weight:700;color:#fff;margin:7px 0 2px}
  .expect p{font-size:6.4px;line-height:1.4;margin-bottom:3px}

  .sessions{padding:20px 16px 0 18px}
  .sessions h4{font-size:8px;font-weight:700;color:var(--leaf);margin-bottom:3px}
  .sessions p{font-size:6.4px;line-height:1.4}
  .cost{position:absolute;left:18px;right:16px;top:300px;color:#fff;text-align:right}
  .cost .studio-name{color:#fff;font-size:14px;justify-content:flex-start;margin-bottom:8px}
  .cost .studio-name .dot{background:#fff}
  .cost h5{font-size:10px;font-weight:700;margin-bottom:3px}
  .cost p{font-size:7px;line-height:1.5}
  .cost .price{font-size:8.5px;font-weight:700}
</style>
</head>
<body>

<!-- Outside of the tri-fold -->
<section class="sheet sheet--outside">
  <svg class="bg" width="690" height="420" viewBox="0 0 690 420">
    <defs>
      <linearGradient id="swoop" x1="0" y1="0" x2="0" y2="1">
        <stop offset="0" stop-color="#8fc330"/><stop offset="1" stop-color="#b5dc3a"/>
      </linearGradient>
      <linearGradient id="coverBg" x1="0" y1="0" x2="1" y2="0">
        <stop offset="0" stop-color="#eef0ec"/><stop offset="1" stop-color="#f8f9f7"/>
      </linearGradient>
    </defs>
    <rect x="230" y="0" width="460" height="420" fill="url(#coverBg)"/>
    <path d="M0,0 H470 C450,70 390,110 300,108 C220,106 190,88 120,96 C60,104 25,130 0,150 Z" fill="url(#swoop)"/>
    <path d="M0,150 C25,130 60,104 120,96 C190,88 220,106 300,108 C390,110 450,70 470,0 L478,0 C460,80 395,120 300,118 C220,116 190,98 120,106 C60,113 25,138 0,160 Z" fill="#d6ea9b"/>
    <line x1="230" y1="0" x2="230" y2="420" stroke="#e2e4e0"/>
    <line x1="460" y1="0" x2="460" y2="420" stroke="#e2e4e0"/>
    <!-- cover photo with curved edge -->
    <path role="img" aria-label="Photo: smiling mature woman stretching on a mat in a bright studio" d="M540,150 H690 V345 H520 C500,300 505,200 540,150 Z" fill="#c9b8a4"/>
    <path d="M540,150 C505,200 500,300 520,345 L505,345 C485,300 492,195 532,150 Z" fill="#9bcb3c"/>
    <path d="M470,300 C500,350 560,365 690,345 V360 C560,380 495,365 470,300 Z" fill="#add136"/>
    <!-- back panel photo -->
    <rect role="img" aria-label="Photo: young woman seated cross-legged holding a dumbbell and a plate of vegetables" x="40" y="250" width="150" height="150" rx="4" fill="#f2e6ea"/>
  </svg>

  <div class="panel p2">
    <div class="back-contact">
      <div class="studio-name"><span class="dot"></span>Evergreen Wellness Studio</div>
      Suite 12<br>Level 2<br>8 Wattle Grove Lane<br>Kingsbury<br>&#9742; 0400 123 456<br>www.evergreenwellness.com.au
    </div>
  </div>

  <div class="panel p3">
    <div class="cover-brand">
      <div class="studio-name"><span class="dot"></span>Evergreen Wellness Studio</div>
      <div class="tagline">Personalised Care in Fitness and Health</div>
    </div>
  </div>
</section>

<!-- Inside of the tri-fold -->
<section class="sheet sheet--inside">
  <svg class="bg" width="690" height="420" viewBox="0 0 690 420">
    <defs>
      <linearGradient id="pale" x1="0" y1="0" x2="0" y2="1">
        <stop offset="0" stop-color="#eaf2ce"/><stop offset="1" stop-color="#cadf82"/>
      </linearGradient>
      <linearGradient id="bright" x1="0" y1="0" x2="0" y2="1">
        <stop offset="0" stop-color="#b7dc42"/><stop offset="1" stop-color="#9bcb3c"/>
      </linearGradient>
      <linearGradient id="paleTop" x1="0" y1="0" x2="0" y2="1">
        <stop offset="0" stop-color="#eef5d6"/><stop offset="1" stop-color="#ffffff"/>
      </linearGradient>
    </defs>
    <rect x="0" y="0" width="230" height="420" fill="url(#pale)"/>
    <rect x="230" y="0" width="230" height="420" fill="url(#bright)"/>
    <rect x="460" y="0" width="230" height="420" fill="url(#paleTop)"/>
    <!-- panel 1 photo arc -->
    <path role="img" aria-label="Photo: women exercising with hand weights in a group class" d="M0,420 V330 C40,270 120,250 230,262 V420 Z" fill="#d9c2b0"/>
    <path d="M0,420 C60,370 150,355 230,370 V395 C150,382 70,395 20,420 Z" fill="#9bcb3c"/>
    <path d="M0,330 C40,270 120,250 230,262 V270 C120,258 45,278 0,340 Z" fill="#add136"/>
    <!-- panel 3 photo band -->
    <path role="img" aria-label="Photo: trainer guiding a client through a balance exercise" d="M460,140 C540,110 620,108 690,118 V290 H460 Z" fill="#3b3f44"/>
    <path d="M460,140 C540,110 620,108 690,118 V126 C620,116 540,118 460,148 Z" fill="#9bcb3c"/>
    <path d="M460,300 C530,260 610,262 690,240 V420 H460 Z" fill="url(#bright)"/>
    <path d="M460,300 C530,260 610,262 690,240 V250 C610,272 530,270 460,310 Z" fill="#d6ea9b"/>
    <line x1="230" y1="0" x2="230" y2="420" stroke="#8fbb33" stroke-opacity=".5"/>
    <line x1="460" y1="0" x2="460" y2="420" stroke="#8fbb33" stroke-opacity=".5"/>
  </svg>

  <div class="panel p1 intro">
    <h2>Personalised Care</h2>
    <h3>in Fitness and Health</h3>
    <p>Exercise programs for all levels of health and fitness and all age groups.</p>
    <p>Experience in managing a wide range of chronic health conditions.</p>
    <h2 class="gap">Experienced Professionals</h2>
    <h3>caring for your wellbeing</h3>
    <p>Exercise Physiologist with over 25 years of experience managing the health and fitness needs of the community.</p>
  </div>

  <div class="panel p2 expect">
    <h2>What to Expect</h2>
    <p>On arrival at the studio you will be asked to complete a questionnaire, which will provide us with information regarding your background with health and fitness, as well as your goals and objectives.</p>
    <p>Please bring any relevant medical information from medical practitioners or health professionals that you feel may impact on your program.</p>
    <h4>Consultation</h4>
    <p>A consultation will allow you to share your thoughts, concerns and objectives, as well as provide you with ample opportunity to expand on the answers from your questionnaire relating to your prior and current health, medical and physical concerns.</p>
    <h4>Assessment</h4>
    <p>An assessment will be conducted to provide us both with a baseline measure of your cardiovascular fitness, strength, flexibility, balance and body composition measures. These measures provide us with a reference for program design and also to indicate improvements along the way.</p>
    <h4>The program</h4>
    <p>Your program will be designed with consideration to your health and fitness background, you objectives and your strengths and weaknesses. It will be personally tailored to your needs and provide you with a plan to focus your energies on.</p>
    <h4>Nutrition</h4>
    <p>Nutrition is central to an effective program, as it will provide you with maximal energy for exercise as well as keeping yourself lean and healthy for a long term fitter lifestyle. The studio provides initial monitoring and ongoing modification in accordance with your needs.</p>
  </div>

  <div class="panel p3">
    <div class="sessions">
      <h4>Your sessions</h4>
      <p>Training at the studio is professional and caring, but focused and challenging. Typically each session will take approximately 60 minutes. Training times can be organised to suit your needs with early mornings and evenings available.</p>
    </div>
    <div class="cost">
      <div class="studio-name"><span class="dot"></span>Evergreen Wellness Studio</div>
      <h5>The Cost</h5>
      <p class="price">$45 paid in blocks of 5 or 10 sessions</p>
      <p>Health fund claimable<br>Open 7 days<br>Ample private parking available</p>
    </div>
  </div>
</section>

</body>
</html>
```